Orva Business Card

we need a business card for flooring business called Orva Flooring, the design should be black and white. we have 2 locations

Nunawading Showroom
527 Kellerman Road,
Nunawading VIC 3131

Bentleigh Showroom
462 Bramwell Hwy,
Bentleigh VIC 3204

email : sales@orvaflooring.com.au
(03) 9471 2830

Please inform we sell , Laminate, Hybrid, Timber, carpet and commercial flooring

```html
<!DOCTYPE html>
<html lang="en">
<head>
<meta charset="utf-8">
<title>Orva Flooring – Business Card</title>
<link href="https://fonts.googleapis.com/css2?family=Open+Sans:wght@300;400;600;700&display=swap" rel="stylesheet">
<style>
  :root {
    --stage: #232323;
    --card: #2a2a2c;
    --card-edge: #f2f2f2;
    --ink: #ffffff;
    --ink-soft: #cfcfcf;
    --ghost: #353538;
    --ghost-line: #1c1c1e;
  }
  * { box-sizing: border-box; margin: 0; padding: 0; }
  html, body { width: 1200px; height: 780px; overflow: hidden; }
  body {
    background: var(--stage);
    font-family: "Open Sans", Arial, sans-serif;
    color: var(--ink);
    display: flex;
    align-items: center;
    justify-content: center;
    gap: 44px;
  }
  .card {
    position: relative;
    width: 540px;
    height: 310px;
    background: var(--card);
    border-radius: 22px;
    box-shadow: 0 0 0 2px var(--card-edge), 0 18px 40px rgba(0,0,0,.6);
    overflow: hidden;
  }

  /* Back side */
  .card-back .brand-mini {
    position: absolute;
    top: 96px; left: 0; right: 0;
    text-align: center;
    font-weight: 400;
    font-size: 22px;
    letter-spacing: 1px;
    color: var(--ink-soft);
  }
  .card-back .brand-mini small {
    display: block;
    font-size: 8px;
    letter-spacing: 2px;
    margin-top: -2px;
  }
  .services {
    position: absolute;
    left: 40px; right: 40px; bottom: 46px;
    text-align: center;
  }
  .services-rule {
    display: flex;
    align-items: center;
    gap: 10px;
    font-size: 11px;
    font-weight: 700;
    letter-spacing: .5px;
    margin-bottom: 8px;
  }
  .services-rule::before, .services-rule::after {
    content: "";
    flex: 1;
    height: 1px;
    background: var(--ink-soft);
  }
  .services-list {
    list-style: none;
    display: flex;
    justify-content: center;
    gap: 6px;
    font-size: 11.5px;
  }
  .services-list li + li::before {
    content: "•";
    margin-right: 6px;
  }

  /* Front side */
  .card-front .brand-block {
    position: absolute;
    left: 34px; top: 22px;
    font-weight: 300;
    line-height: 1;
  }
  .brand-block .brand-name { font-size: 40px; letter-spacing: 1px; }
  .brand-block .brand-sub { font-size: 20px; letter-spacing: 1px; margin-top: 4px; display: block; }
  .title-block {
    position: absolute;
    top: 24px; right: 46px;
    text-align: right;
  }
  .title-block h1 { font-size: 22px; font-weight: 700; line-height: 1.1; }
  .title-block p { font-size: 12px; }
  .title-bar {
    position: absolute;
    top: 18px; right: 22px;
    width: 14px; height: 54px;
    background: var(--ink);
  }
  .ghost-mark {
    position: absolute;
    right: 24px; bottom: 50px;
    font-size: 96px;
    font-weight: 300;
    color: var(--ghost);
    text-shadow: 1px 1px 0 var(--ghost-line);
    line-height: 1;
  }
  .contact {
    position: absolute;
    left: 62px; top: 108px;
    font-size: 11.5px;
    line-height: 1.35;
  }
  .showroom + .showroom { margin-top: 8px; }
  .showroom h2 { font-size: 12.5px; font-weight: 600; }
  .lines { list-style: none; margin-top: 8px; }
  .lines li { display: flex; align-items: center; gap: 8px; margin-top: 2px; }
  .lines svg { width: 12px; height: 12px; flex: none; }
  .lines .phone { font-size: 15px; font-weight: 700; }
</style>
</head>
<body>

  <section class="card card-back" aria-label="Card back">
    <div class="brand-mini">Orva<small>FLOORING</small></div>
    <div class="services">
      <div class="services-rule">WE SELL</div>
      <ul class="services-list">
        <li>Laminate</li><li>Hybrid</li><li>Timber</li><li>Carpet</li><li>Commercial flooring</li>
      </ul>
    </div>
  </section>

  <section class="card card-front" aria-label="Card front">
    <div class="brand-block">
      <span class="brand-name">Orva</span>
      <span class="brand-sub">FLOORING</span>
    </div>

    <div class="title-bar"></div>
    <div class="title-block">
      <h1>Orva Flooring</h1>
      <p>Carpet &amp; Flooring Store</p>
    </div>

    <div class="ghost-mark" aria-hidden="true">Orva</div>

    <address class="contact" style="font-style:normal">
      <div class="showroom">
        <h2>Nunawading Showroom</h2>
        <p>527 Kellerman Road, Nunawading<br>VIC 3131</p>
      </div>
      <div class="showroom">
        <h2>Bentleigh Showroom</h2>
        <p>462 Bramwell Hwy, Bentleigh<br>VIC 3204</p>
      </div>
      <ul class="lines">
        <li>
          <svg viewBox="0 0 24 24" aria-hidden="true"><path fill="#fff" d="M6.6 10.8a15 15 0 0 0 6.6 6.6l2.2-2.2a1 1 0 0 1 1-.25 11.4 11.4 0 0 0 3.6.57 1 1 0 0 1 1 1V20a1 1 0 0 1-1 1A17 17 0 0 1 3 4a1 1 0 0 1 1-1h3.5a1 1 0 0 1 1 1c0 1.25.2 2.45.57 3.57a1 1 0 0 1-.25 1z"/></svg>
          <span class="phone">(03) 9471 2830</span>
        </li>
        <li>
          <svg viewBox="0 0 24 24" aria-hidden="true"><circle cx="12" cy="12" r="9" fill="none" stroke="#fff" stroke-width="2"/><path d="M3 12h18M12 3c3 3 3 15 0 18M12 3c-3 3-3 15 0 18" fill="none" stroke="#fff" stroke-width="1.5"/></svg>
          <span>www.orvaflooring.com.au</span>
        </li>
        <li>
          <svg viewBox="0 0 24 24" aria-hidden="true"><rect x="3" y="6" width="18" height="12" rx="1" fill="none" stroke="#fff" stroke-width="2"/><path d="M3 7l9 6 9-6" fill="none" stroke="#fff" stroke-width="2"/></svg>
          <span>sales@orvaflooring.com.au</span>
        </li>
      </ul>
    </address>
  </section>

</body>
</html>
```